Emerging Australian photographer

I'm based in Cunderdin, a small rural town in the Wheatbelt area of Western Australia. So its a good thing that I love to travel further afield both for pleasure and for work. To me that is one and the same thing in any event!

My desire is to take photos that make the viewers heart skip. I love taking photos of people doing the things they love or being with the people they love. For me, the joy of photography comes with capturing the 'moments between the moments'. I like candid photography best of all - like when the new husband is staring joyfully at his bride and at that minute is unaware of the photographer capturing the moment.

I am available for weddings, engagements, birthdays, special events, newborns, family or individual portraits. By the end of the year I will be accredited with the Coastal Guild of Image Artisans.

I need a card that stands out but is elegant and would sit well on the table at a wedding or be given out in the church grounds. Classy and a little bit sassy.

Target Market(s)

Consumers who are seeking photographic services, eg wedding guests who see me at work and make enquiries.

Industry/Entity Type

Church

Contact Information for Business Card

Tamsin Bexley Photography
Tamsin Bexley
0452 307 618
www.tamsinbexley.com.au
photos@tamsinbexley.com.au

Requirements
Must have
• Must fit with the theme in the watermarks, but be crisp and modern.
Nice to have
• However it's not essential to have the pink! Facebook and Twitter logos.
Should not have
• Old style fonts like times new roman.

```html
<!DOCTYPE html>
<html lang="en">
<head>
<meta charset="utf-8">
<title>Tamsin Bexley Photography – Business Card</title>
<link rel="stylesheet" href="https://fonts.googleapis.com/css2?family=Arimo:wght@400;700&display=swap">
<style>
  :root {
    --blush: #f3b4cd;
    --blush-deep: #ee7fae;
    --blush-faint: rgba(243, 180, 205, 0.30);
    --blush-fade: rgba(243, 180, 205, 0);
    --charcoal: #5f5f63;
    --ink: #3f3f44;
    --paper: #ffffff;
    --backdrop: #ece9e6;
    --card-shadow: rgba(60, 50, 45, 0.18);
  }
  * { margin: 0; padding: 0; box-sizing: border-box; }
  html, body {
    width: 916px;
    height: 1200px;
    overflow: hidden;
    background: var(--backdrop);
    font-family: "Arimo", Arial, sans-serif;
  }
  .canvas {
    position: relative;
    width: 916px;
    height: 1200px;
  }
  .card {
    position: absolute;
    left: 78px;
    width: 760px;
    height: 434px;
    border-radius: 26px;
    box-shadow: 0 10px 28px var(--card-shadow);
    overflow: hidden;
  }
  .card--front { top: 140px; background: var(--blush); }
  .card--back { top: 626px; background: var(--paper); }

  /* Brand name */
  .brand {
    display: flex;
    align-items: center;
    gap: 14px;
  }
  .brand__dot {
    width: 16px;
    height: 16px;
    border-radius: 50%;
    flex: none;
  }
  .brand__name {
    font-weight: 400;
    text-transform: lowercase;
    letter-spacing: 0.02em;
  }

  /* Front */
  .card--front .brand {
    position: absolute;
    left: 0; right: 0;
    top: 168px;
    justify-content: center;
  }
  .card--front .brand__dot { background: var(--paper); }
  .card--front .brand__name { color: var(--paper); font-size: 46px; }
  .website {
    position: absolute;
    left: 0; right: 0;
    top: 268px;
    text-align: center;
    color: var(--paper);
    font-size: 17px;
    letter-spacing: 0.34em;
  }

  /* Back */
  .watermark {
    position: absolute;
    left: 30px;
    right: 30px;
    top: 30px;
    bottom: 20px;
    border-radius: 40px;
    background:
      radial-gradient(ellipse 42% 55% at 30% 55%, var(--blush-faint), var(--blush-fade) 70%),
      radial-gradient(ellipse 40% 50% at 68% 48%, var(--blush-faint), var(--blush-fade) 70%);
  }
  .card--back .brand {
    position: absolute;
    left: 110px;
    top: 60px;
  }
  .card--back .brand__dot { background: var(--blush-deep); width: 12px; height: 12px; }
  .card--back .brand__name { color: var(--charcoal); font-size: 28px; }

  .contact {
    position: absolute;
    right: 58px;
    bottom: 56px;
    text-align: left;
  }
  .contact__name {
    font-size: 34px;
    font-weight: 400;
    line-height: 1;
  }
  .contact__first { color: var(--blush-deep); }
  .contact__last { color: var(--ink); }
  .contact__role {
    color: var(--blush-deep);
    font-size: 15px;
    letter-spacing: 0.42em;
    margin: 6px 0 16px 2px;
  }
  .contact__line {
    font-size: 15px;
    line-height: 1.55;
    color: var(--ink);
  }
  .contact__label {
    color: var(--blush-deep);
    margin-right: 6px;
  }
</style>
</head>
<body>
  <main class="canvas">
    <section class="card card--front" aria-label="Card front">
      <div class="brand">
        <span class="brand__dot"></span>
        <span class="brand__name">Tamsin Bexley Photography</span>
      </div>
      <p class="website">www.tamsinbexley.com.au</p>
    </section>

    <section class="card card--back" aria-label="Card back">
      <div class="watermark" role="img" aria-label="Large faint pink decorative flourish spanning the card"></div>
      <div class="brand">
        <span class="brand__dot"></span>
        <span class="brand__name">Tamsin Bexley Photography</span>
      </div>
      <div class="contact">
        <h1 class="contact__name"><span class="contact__first">Tamsin</span> <span class="contact__last">Bexley</span></h1>
        <p class="contact__role">Photographer</p>
        <p class="contact__line"><span class="contact__label">Phone</span>0452 307 618</p>
        <p class="contact__line"><span class="contact__label">Email</span>photos@tamsinbexley.com.au</p>
      </div>
    </section>
  </main>
</body>
</html>
```